Business Card - Tally Forge

Need Business Card design for company named Tally Forge. Software development focused mainly on Brindle Kelvox & Vuro Apps. I've attached our logo with both a black and white background. Please add trademark symbol to logo when using.

```html
<!DOCTYPE html>
<html lang="en">
<head>
<meta charset="utf-8">
<title>Tally Forge – Business Card</title>
<link rel="stylesheet" href="https://fonts.googleapis.com/css2?family=Exo+2:wght@600&family=Open+Sans:wght@400&display=swap">
<style>
  :root {
    --backdrop: #d9d9d7;
    --paper: #f4f4f2;
    --ink: #2b2b2b;
    --night: #050505;
    --night-mark: #3a3a3a;
    --gold: #e6b012;
    --amber: #de7a1c;
    --crimson: #d2232a;
    --white: #ffffff;
  }
  * { margin: 0; padding: 0; box-sizing: border-box; }
  html, body {
    width: 1200px; height: 855px; overflow: hidden;
    background: var(--backdrop);
  }
  .sheet {
    position: relative; width: 1200px; height: 855px;
    display: flex; align-items: center; justify-content: center; gap: 40px;
  }
  .card {
    position: relative; width: 540px; height: 309px;
    border-radius: 4px; overflow: hidden;
    box-shadow: 0 6px 18px rgba(0,0,0,0.18);
  }

  /* Front */
  .card--front { background: var(--paper); }
  .bands { position: absolute; inset: 0 auto 0 0; display: flex; height: 100%; }
  .band { width: 58px; height: 100%; }
  .band--gold { background: var(--gold); }
  .band--amber { background: var(--amber); }
  .band--crimson { background: var(--crimson); }
  .front-mark {
    position: absolute; left: 22px; top: 58px;
    display: flex; align-items: center; gap: 8px;
    font-family: "Exo 2", sans-serif; font-weight: 600;
    font-size: 20px; color: var(--white); letter-spacing: -0.2px;
  }
  .front-mark .square { width: 14px; height: 14px; background: var(--white); }
  .identity {
    position: absolute; left: 270px; top: 150px; width: 250px;
  }
  .company {
    font-family: "Exo 2", sans-serif; font-weight: 600;
    font-size: 42px; line-height: 1; color: var(--ink); letter-spacing: -1px;
    margin-bottom: 10px;
  }
  .contact {
    font-family: "Open Sans", sans-serif; font-size: 12px; line-height: 1.45;
  }
  .contact-lines { display: flex; gap: 18px; }
  .phone { color: var(--gold); }
  .fax { color: var(--amber); }
  .address { color: var(--crimson); margin-left: 104px; margin-top: 4px; }

  /* Back */
  .card--back {
    background: var(--night);
    display: flex; align-items: center; justify-content: center;
  }
  .back-mark {
    display: flex; align-items: center; gap: 10px;
    font-family: "Exo 2", sans-serif; font-weight: 600;
    font-size: 30px; color: var(--night-mark); letter-spacing: -0.5px;
  }
  .back-mark .square { width: 20px; height: 20px; background: var(--amber); }
</style>
</head>
<body>
  <main class="sheet">
    <section class="card card--front" aria-label="Business card front">
      <div class="bands" aria-hidden="true">
        <span class="band band--gold"></span>
        <span class="band band--amber"></span>
        <span class="band band--crimson"></span>
      </div>
      <div class="front-mark"><span class="square"></span>Tally Forge™</div>
      <div class="identity">
        <h1 class="company">Tally Forge</h1>
        <div class="contact">
          <div class="contact-lines">
            <span class="phone">P. 555-014-2290</span>
            <span class="fax">F. 555-014-7713</span>
          </div>
          <p class="address">4120 Harbor Mill Rd<br>Cedar Bend, FL 30419</p>
        </div>
      </div>
    </section>

    <section class="card card--back" aria-label="Business card back">
      <div class="back-mark"><span class="square"></span>Tally Forge™</div>
    </section>
  </main>
</body>
</html>
```